Business Cards for a law firm

Business cards for our law firm. Use our silhoette logo and OAK HARBOR - check our website (www.oakharbor-legal.com)

Contact Information for Business Card

our silhouette logo, OAK HARBOR, 800-555-0147, Dorian Kestrup, dorian@oakharbor-legal.com

Requirements
Must have
• our silhouette logo, OAK HARBOR, 800-555-0147, Dorian Kestrup, dorian@oakharbor-legal.com

```html
<!DOCTYPE html>
<html lang="en">
<head>
<meta charset="utf-8">
<title>Oak Harbor – Business Card</title>
<link rel="stylesheet" href="https://fonts.googleapis.com/css2?family=Montserrat:wght@500&family=Roboto:wght@400;500&display=swap">
<style>
  :root {
    --backdrop: #263159;
    --card: #ffffff;
    --ink: #253162;
    --accent: #f6a821;
    --on-accent: #ffffff;
  }
  * { margin: 0; padding: 0; box-sizing: border-box; }
  html, body {
    width: 1200px;
    height: 1000px;
    overflow: hidden;
    background: var(--backdrop);
  }
  .canvas {
    position: relative;
    width: 1200px;
    height: 1000px;
    background: var(--backdrop);
  }
  .business-card {
    position: absolute;
    left: 207px;
    top: 278px;
    width: 786px;
    height: 445px;
    background: var(--card);
    color: var(--ink);
  }
  .brand-mark {
    position: absolute;
    left: 140px;
    top: 128px;
    width: 46px;
    height: 46px;
    background: var(--ink);
  }
  .brand-name {
    position: absolute;
    left: 205px;
    top: 122px;
    font-family: "Montserrat", sans-serif;
    font-weight: 500;
    font-size: 54px;
    line-height: 1;
    letter-spacing: 2px;
    color: var(--ink);
    white-space: nowrap;
  }
  .brand-rule {
    position: absolute;
    left: 205px;
    top: 196px;
    width: 430px;
    height: 2px;
    background: var(--ink);
  }
  .phone-band {
    position: absolute;
    left: 16px;
    top: 366px;
    width: 387px;
    height: 63px;
    background: var(--accent);
    display: flex;
    align-items: center;
    padding-left: 24px;
  }
  .phone-number {
    font-family: "Roboto", sans-serif;
    font-weight: 500;
    font-size: 40px;
    color: var(--on-accent);
    letter-spacing: 0.5px;
  }
  .contact {
    position: absolute;
    left: 429px;
    top: 352px;
    font-family: "Roboto", sans-serif;
    font-weight: 400;
    font-size: 22px;
    line-height: 30px;
    color: var(--ink);
  }
</style>
</head>
<body>
  <main class="canvas">
    <section class="business-card" aria-label="Oak Harbor business card">
      <div class="brand-mark" aria-hidden="true"></div>
      <h1 class="brand-name">OAK HARBOR</h1>
      <div class="brand-rule" aria-hidden="true"></div>

      <div class="phone-band">
        <span class="phone-number">800-555-0147</span>
      </div>

      <address class="contact" style="font-style: normal;">
        <div class="contact-name">Dorian Kestrup</div>
        <div class="contact-email">dorian@oakharbor-legal.com</div>
      </address>
    </section>
  </main>
</body>
</html>
```